Corvelle Strategies business card

I need a business card for my new strategic consulting LLC, Corvelle Strategies. We specialize in helping people who care about broadband technology and telecommunications policy, and we're based in Washington DC. I'm looking for a card that says smart, credible, future-facing and signals a high level of expertise. It's DC, so there's clearly a limit to how crazy we can go with this card, but I am looking for a design that reflects a company that is comfortable with technology, policy, and having a little bit fun. I'm uploading my logo below, and I'd like to have it be part of the card design in some fashion.
Target Market(s)
Telecommunications and technology policy professionals
Industry/Entity Type
Technology policy
Contact Information for Business Card
Name of business, my name (Glen Mosswater), email (glen@corvellestrategies-example.com) , phone number (202-555-0148)phone number

```html
<!DOCTYPE html>
<html lang="en">
<head>
<meta charset="utf-8">
<title>Corvelle Strategies business card</title>
<link rel="stylesheet" href="https://fonts.googleapis.com/css2?family=Merriweather:wght@400;700;900&display=swap">
<style>
  :root {
    --backdrop: #3a3a3c;
    --card: #f7f7f7;
    --card-shade: #e6e6e6;
    --brand-blue: #07509a;
    --brand-blue-deep: #053f7a;
    --sun-orange: #f2ab3c;
    --ink: #444a52;
  }
  * { box-sizing: border-box; margin: 0; padding: 0; }
  html, body {
    width: 1200px; height: 900px; overflow: hidden;
    background: var(--backdrop);
    font-family: "Merriweather", Georgia, serif;
  }
  .canvas { position: relative; width: 1200px; height: 900px; }
  .card {
    position: absolute;
    width: 560px; height: 320px;
    background: linear-gradient(120deg, var(--card) 0%, #ececec 55%, var(--card) 100%);
    box-shadow: 0 14px 30px rgba(0,0,0,.45);
    overflow: hidden;
  }
  .card-front { left: 80px; top: 90px; display: flex; align-items: center; justify-content: center; }
  .card-back { left: 560px; top: 490px; }

  .brand-name {
    font-weight: 900;
    font-size: 38px;
    color: var(--brand-blue);
    letter-spacing: -0.5px;
    display: flex; align-items: center; gap: 14px;
  }
  .brand-dot {
    width: 22px; height: 22px; border-radius: 50%;
    background: var(--sun-orange);
  }

  .contact-block { position: absolute; left: 30px; top: 58px; }
  .person-name {
    font-weight: 900; font-size: 17px;
    color: var(--brand-blue); text-transform: uppercase;
    letter-spacing: -0.3px; margin-bottom: 18px;
  }
  .contact-line {
    display: flex; align-items: center; gap: 9px;
    font-size: 11px; color: var(--ink); margin-bottom: 8px;
  }
  .contact-line svg { width: 14px; height: 14px; flex: none; }

  .mark-field {
    position: absolute; right: 0; top: 0;
    width: 300px; height: 320px;
    background: linear-gradient(160deg, var(--sun-orange) 0%, var(--sun-orange) 18%, var(--brand-blue) 42%, var(--brand-blue-deep) 100%);
    clip-path: polygon(22% 0, 100% 0, 100% 100%, 0 100%);
  }
</style>
</head>
<body>
<main class="canvas">
  <section class="card card-front" aria-label="Card front">
    <div class="brand-name"><span>Corvelle Strategies</span><span class="brand-dot"></span></div>
  </section>

  <section class="card card-back" aria-label="Card back">
    <div class="contact-block">
      <p class="person-name">Glen Mosswater</p>
      <p class="contact-line">
        <svg viewBox="0 0 24 24" aria-hidden="true"><path fill="#f2ab3c" d="M6.6 10.8a15.1 15.1 0 0 0 6.6 6.6l2.2-2.2a1 1 0 0 1 1-.25 11.4 11.4 0 0 0 3.6.57 1 1 0 0 1 1 1V20a1 1 0 0 1-1 1A17 17 0 0 1 3 4a1 1 0 0 1 1-1h3.5a1 1 0 0 1 1 1c0 1.25.2 2.45.57 3.57a1 1 0 0 1-.25 1z"/></svg>
        <span>202-555-0148</span>
      </p>
      <p class="contact-line">
        <svg viewBox="0 0 24 24" aria-hidden="true"><rect x="2" y="5" width="20" height="14" rx="1" fill="#f2ab3c"/><path d="M2.5 5.5 12 13l9.5-7.5" fill="none" stroke="#fff" stroke-width="1.6"/></svg>
        <span>glen@corvellestrategies-example.com</span>
      </p>
    </div>
    <div class="mark-field" role="img" aria-label="Large brand emblem artwork: sun over mountain peaks and a river"></div>
  </section>
</main>
</body>
</html>
```